WP website design (Vorne)

We need a wordpress design for an established auction and real estate company based in Kentucky. The winning design will incorporate a professional color scheme with company logo in a clean layout with specified widgets. The design needs to consider that this will be developed on a responsive theme. Colors will complement the colors in the logo.

Industry/Entity Type

Real Estate

Font styles to use
Sans Serif

Requirements
Must have
• - Navigation:
1) Home 2) Auctions 3) Real Estate Listings 4) Our Services 5) Why Auctions 6) About Us 7) Past Auctions 8) Contact Us

Homeage will have slideshow, please use stock real estate image as the initial slide. Homepage will have this content: "Martin Vorne Auctioneer Real Estate Broker

Buying or selling you can count on Martin Vorne Auctioneer to deliver a quality auction experience. We handle all the details from initial handshake to final payment. We are with you every step of the way giving our sellers the service and results they deserve. You only have one chance for a successful auction. Contact us today to see how our experience and know-how can work for you. We are confident that you will appreciate our higher standard of service."

Footer will have smaller company logo, and attached association logos and this contact info:
Phone: (270) 555-0148
Contacts: Martin Vorne
Email: martinvorne@mailbrook.example
Address: 482 Pellworth Lane • Bowling Green, KY 42917

Widgets:
1) email sign up 2) Social media (twitter, Youtube - can also be in header 3) News & Events Blog widget 4) testimonials blog 5) Featured Video widget
Nice to have
• Nice to Have:
- demonstrate the drop-down menu styling, e.g. under Auctions
-Upcoming Auctions
-Online Auctions
-Past Auctions

```html
<!DOCTYPE html>
<html lang="en">
<head>
<meta charset="utf-8">
<title>Martin Vorne Auctioneer Real Estate Broker</title>
<link href="https://fonts.googleapis.com/css2?family=Arvo:wght@400;700&family=PT+Sans:wght@400;700&family=Source+Sans+3:wght@400;600;700&display=swap" rel="stylesheet">
<style>
:root{
  --blue:#2a64ad;
  --blue-dark:#1d4f93;
  --blue-nav-top:#3572bb;
  --blue-nav-bot:#1f58a0;
  --yellow:#e8b81f;
  --yellow-text:#e9b824;
  --grey-top:#e9e9e9;
  --page:#f7f8f8;
  --band:#ececec;
  --footer:#e4e4e4;
  --text:#7d7d7d;
  --text-dark:#555;
}
*{box-sizing:border-box;margin:0;padding:0}
html,body{width:955px;height:1200px;overflow:hidden}
body{position:relative;background:var(--page);font-family:"PT Sans",sans-serif;color:var(--text)}
.abs{position:absolute}
.top-band{left:0;top:0;width:955px;height:369px;background:var(--grey-top);border-bottom:1px solid #dcdcdc}
.brand{left:127px;top:0;width:95px;height:96px;background:#fff;border-radius:0 0 4px 4px;box-shadow:0 1px 3px rgba(0,0,0,.15);display:flex;flex-direction:column;align-items:center;justify-content:center;gap:5px}
.brand .mark{width:16px;height:16px;background:var(--yellow)}
.brand .name{font-family:"Source Sans 3",sans-serif;font-weight:700;font-size:13px;color:var(--blue);text-align:center;line-height:1.05}
.social{display:flex;gap:8px}
.social span{width:26px;height:26px;border-radius:3px;display:block}
.s1{background:#3a5a98}.s2{background:#3aa1db}.s3{background:#1f6f99}.s4{background:#d6392b}
.header-social{left:700px;top:21px}
.call{right:124px;top:62px;font-family:"Source Sans 3",sans-serif;font-size:20px;color:#9a9a9a;display:flex;align-items:center;gap:5px}
.call b{font-weight:400;color:var(--blue)}
.nav{left:0;top:102px;width:955px;height:37px;background:linear-gradient(var(--blue-nav-top),var(--blue-nav-bot))}
.nav ul{list-style:none;position:absolute;left:128px;top:0;display:flex;height:37px;border-left:1px solid rgba(0,0,0,.15)}
.nav li{height:37px;line-height:37px;padding:0 15px;font-family:"Source Sans 3",sans-serif;font-weight:700;font-size:11px;color:#fff;border-right:1px solid rgba(0,0,0,.15)}
.nav li.active{background:var(--blue-dark)}
.hero{left:127px;top:145px;width:701px;height:327px;background:linear-gradient(180deg,#4c83c4 0%,#8a9aa0 30%,#6f6257 55%,#2f6f78 75%,#1e4f5c 100%)}
.caption{left:127px;top:298px;width:404px;height:88px;background:rgba(20,40,60,.65)}
.caption h1{position:absolute;left:60px;top:12px;font-family:"Arvo",serif;font-weight:400;font-size:28px;color:#fff}
.caption p{position:absolute;left:60px;top:52px;font-family:"Arvo",serif;font-size:13px;letter-spacing:1px;color:var(--yellow-text);text-transform:uppercase}
.dots{left:452px;top:454px;display:flex;gap:7px}
.dots i{width:8px;height:8px;border-radius:50%;background:rgba(255,255,255,.5)}
.dots i:first-child{background:#fff}
.dropdown{left:196px;top:139px;width:133px;height:74px;background:rgba(33,86,160,.95);list-style:none;padding-top:5px}
.dropdown li{font-family:"Source Sans 3",sans-serif;font-size:10.5px;color:#fff;height:21px;line-height:21px;padding-left:13px}
.dropdown li::before{content:"›";margin-right:6px}
.intro-title{left:128px;top:497px;width:352px;white-space:nowrap;font-family:"Arvo",serif;font-weight:400;font-size:16px;color:var(--blue)}
.intro-text{left:128px;top:528px;width:350px;font-size:10.4px;line-height:15px}
.intro-text p+p{margin-top:15px}
.video{left:488px;top:498px;width:343px;height:172px;border-radius:3px;overflow:hidden;background:linear-gradient(180deg,#7aa8d8 0%,#9a8a70 40%,#c9b898 65%,#5f7a45 100%)}
.video .play{position:absolute;left:148px;top:54px}
.video .bar{position:absolute;left:0;bottom:0;width:100%;height:29px;background:rgba(0,0,0,.8)}
.video .bar svg{position:absolute;left:0;top:0}
.video .time{position:absolute;left:252px;top:9px;font-family:"Source Sans 3",sans-serif;font-size:8px;color:#fff}
.divider{left:127px;top:698px;width:701px;border-top:3px dotted #d3d3d3}
.col-title{font-family:"Arvo",serif;font-weight:400;font-size:15px;color:var(--blue)}
.avatar{left:128px;top:766px;width:38px;height:38px;background:linear-gradient(#c9a080,#7b5a44);border:1px solid #ddd}
.person{left:177px;top:767px;font-family:"Source Sans 3",sans-serif;font-size:13.5px;color:var(--text-dark)}
.person small{display:block;font-size:9.5px;color:#aaa;margin-top:2px}
.quote{left:129px;top:825px;width:186px;height:81px;background:var(--blue);border-radius:2px;box-shadow:0 1px 3px rgba(0,0,0,.2);padding:14px 10px 0 30px;font-size:10.5px;line-height:18px;color:#fff}
.quote::before{content:"";position:absolute;left:13px;top:-8px;border:8px solid transparent;border-bottom-color:var(--blue);border-left-width:0;border-top-width:0}
.quote::after{content:"\201C";position:absolute;left:11px;top:8px;font-family:"Arvo",serif;font-size:24px;line-height:24px;font-weight:700}
.news{left:369px;top:763px;width:215px}
.news-item{display:flex;gap:15px;margin-bottom:12px;height:40px}
.news-item .thumb{width:40px;height:40px;flex:none}
.t1{background:linear-gradient(#8a9aa8,#3d4650)}.t2{background:linear-gradient(#d9d2ca,#8a7566)}.t3{background:linear-gradient(#6aa0d8,#5d7a4a)}
.news-item p{font-size:8.6px;line-height:15px;color:#999;margin-top:-4px}
.news-item time{display:block;color:var(--text-dark)}
.signup{left:604px;top:731px;width:224px;height:181px;background:#e8e8e8;border:1px solid #dadada}
.signup h3{position:absolute;left:20px;top:17px;font-family:"Arvo",serif;font-weight:400;font-size:13px;color:var(--blue)}
.signup .field{position:absolute;left:19px;top:43px;width:190px;height:28px;background:#fff;border:1px solid #d8d8d8;font-size:9.5px;color:#aaa;line-height:26px;padding-left:12px}
.signup .field b{color:var(--yellow)}
.signup .check{position:absolute;left:19px;top:82px;width:18px;height:18px;border-radius:2px;background:var(--blue)}
.signup .check-label{position:absolute;left:46px;top:82px;width:170px;font-size:9.6px;line-height:15px;color:var(--text)}
.signup .btn{position:absolute;left:19px;top:122px;width:189px;height:32px;border-radius:3px;background:linear-gradient(#f0c63a,#dcab12);font-family:"Arvo",serif;font-weight:700;font-size:9.5px;color:#fff;text-align:center;line-height:32px;box-shadow:0 1px 2px rgba(0,0,0,.25)}
.partners{left:0;top:938px;width:955px;height:91px;background:var(--band);border-bottom:1px solid #d6d6d6}
.badge{position:absolute;background:#b3b3b3}
.footer{left:0;top:1030px;width:955px;height:136px;background:var(--footer)}
.footer .brand{top:22px;left:133px;width:97px;height:88px;border-radius:4px;box-shadow:none;border:1px solid #d5d5d5}
.fcol{position:absolute;top:24px}
.fcol h4{font-family:"Source Sans 3",sans-serif;font-weight:400;font-size:11px;color:#666;margin-bottom:7px}
.fcol ul{list-style:none}
.fcol li{font-size:7.6px;color:#888;height:18px;line-height:18px}
.fcol.links li::before{content:"";display:inline-block;border:3px solid transparent;border-left:4px solid #888;margin-right:6px}
.fcol li.on{color:#d18b12}
.fcol.contact li{display:flex;align-items:center;gap:9px;height:22px}
.fcol.contact li svg{flex:none}
.footer .social{position:absolute;left:687px;top:48px}
.bottom{left:0;top:1166px;width:955px;height:34px;background:var(--blue-dark);font-family:"Source Sans 3",sans-serif;font-size:8px;color:#fff}
.bottom .copy{position:absolute;left:130px;top:11px}
.bottom .legal{position:absolute;right:142px;top:11px}
</style>
</head>
<body>
<div class="abs top-band"></div>

<header>
  <div class="abs brand"><span class="mark"></span><span class="name">Martin<br>Vorne</span></div>
  <div class="abs social header-social" aria-label="Social links"><span class="s1"></span><span class="s2"></span><span class="s3"></span><span class="s4"></span></div>
  <div class="abs call">
    <svg width="16" height="16" viewBox="0 0 16 16" aria-hidden="true"><path d="M4 1l3 3-2 2c1 2 3 4 5 5l2-2 3 3-2 2C8 14 2 8 2 3z" fill="#a8a8a8"/></svg>
    Call us: <b>1800 555 01 472</b>
  </div>
</header>

<nav class="abs nav">
  <ul>
    <li style="padding:0 24px">Home</li><li class="active">Auctions</li><li style="padding:0 24px">Real Estate Listings</li><li style="padding:0 22px">Buyers</li><li style="padding:0 22px">Sellers</li><li style="padding:0 18px">Brokers</li><li style="padding:0 18px">About</li><li style="padding:0 16px">Contact</li>
  </ul>
</nav>

<section>
  <div class="abs hero" role="img" aria-label="Modern two-storey house with lit windows beside a pool at dusk"></div>
  <div class="abs caption"><h1>Martin Vorne</h1><p>Auctioneer Real Estate Broker</p></div>
  <div class="abs dots"><i></i><i></i><i></i><i></i></div>
  <ul class="abs dropdown"><li>Upcoming Auctions</li><li>Online Auctions</li><li>Past Auctions</li></ul>
</section>

<section>
  <h2 class="abs intro-title">Martin Vorne Auctioneer Real Estate Broker</h2>
  <div class="abs intro-text">
    <p>Buying or selling you can count on Martin Vorne Auctioneer to deliver a quality auction experience. We handle all the details from initial handshake to final payment. We are with you every step of the way giving our sellers the service and results they deserve. You only have one chance for a successful auction.</p>
    <p>Contact us today to see how our experience and know-how can work for you. We are confident that you will appreciate our higher standard of service.</p>
  </div>
  <div class="abs video" role="img" aria-label="Featured video still of a brick house with tiled roof">
    <svg class="play" width="50" height="50" viewBox="0 0 50 50" aria-hidden="true"><circle cx="25" cy="25" r="22" fill="none" stroke="#fff" stroke-width="4"/><path d="M20 15l14 10-14 10z" fill="#fff"/></svg>
    <div class="bar">
      <svg width="343" height="29" viewBox="0 0 343 29" aria-hidden="true">
        <circle cx="23" cy="15" r="6" fill="none" stroke="#fff" stroke-width="1.5"/><path d="M21 12l5 3-5 3z" fill="#fff"/>
        <path d="M41 12h3l4-3v12l-4-3h-3z" fill="#fff"/>
        <g fill="#fff"><rect x="56" y="11" width="1.5" height="8"/><rect x="59" y="11" width="1.5" height="8"/><rect x="62" y="11" width="1.5" height="8"/><rect x="65" y="11" width="1.5" height="8"/><rect x="68" y="11" width="1.5" height="8" opacity=".4"/><rect x="71" y="11" width="1.5" height="8" opacity=".4"/></g>
        <rect x="91" y="14" width="150" height="3" fill="#555"/><rect x="91" y="14" width="53" height="3" fill="#e8b81f"/>
        <rect x="307" y="11" width="10" height="8" fill="none" stroke="#fff" stroke-width="1.5"/>
        <circle cx="332" cy="15" r="4" fill="none" stroke="#fff" stroke-width="2.5" stroke-dasharray="2 1.2"/>
      </svg>
      <span class="time">01:30 / 04:55</span>
    </div>
  </div>
</section>

<div class="abs divider"></div>

<section>
  <h3 class="abs col-title" style="left:128px;top:731px">Client Testimonial</h3>
  <div class="abs avatar" role="img" aria-label="Client portrait photo"></div>
  <div class="abs person">Owen Hartley<small>Businessman</small></div>
  <blockquote class="abs quote">Mauris urnaei elit, mattis non urna acem, ullamcorper ipsum dolor vula putatem lorem.</blockquote>

  <h3 class="abs col-title" style="left:369px;top:731px">Latest News</h3>
  <div class="abs news">
    <div class="news-item"><div class="thumb t1" role="img" aria-label="News photo of business people"></div><p>Nunc purus orci, adipiscing non ipsum non, pellentesque fringilla sapien.<time>October 15, 2013</time></p></div>
    <div class="news-item"><div class="thumb t2" role="img" aria-label="News photo of a woman"></div><p>Nunc purus orci, adipiscing non ipsum non, pellentesque fringilla sapien.<time>October 15, 2013</time></p></div>
    <div class="news-item"><div class="thumb t3" role="img" aria-label="News photo of a house"></div><p>Nunc purus orci, adipiscing non ipsum non, pellentesque fringilla sapien.<time>October 15, 2013</time></p></div>
  </div>

  <div class="abs signup">
    <h3>Signup for our Newletter</h3>
    <div class="field">Enter Your Email <b>*</b></div>
    <div class="check"><svg width="18" height="18" viewBox="0 0 18 18" aria-hidden="true"><path d="M5 9l3 3 5-6" fill="none" stroke="#fff" stroke-width="2"/></svg></div>
    <div class="check-label">To get notified of specific auctions, auction types or locations</div>
    <div class="btn">SUBSCRIBE NOW</div>
  </div>
</section>

<section class="abs partners" aria-label="Associations">
  <div class="badge" style="left:134px;top:17px;width:92px;height:60px;border-radius:50%"></div>
  <div class="badge" style="left:304px;top:23px;width:76px;height:42px;border-radius:4px"></div>
  <div class="badge" style="left:458px;top:24px;width:100px;height:40px"></div>
  <div class="badge" style="left:645px;top:17px;width:50px;height:58px;border-radius:4px"></div>
  <div class="badge" style="left:782px;top:17px;width:40px;height:40px"></div>
</section>

<footer class="abs footer">
  <div class="brand abs"><span class="mark"></span><span class="name">Martin<br>Vorne</span></div>
  <div class="fcol links" style="left:290px"><h4>Navigation</h4><ul><li>Home</li><li>About</li><li>Services</li><li>Contact</li></ul></div>
  <div class="fcol links" style="left:406px"><h4>Auctions</h4><ul><li class="on">Upcoming Auctions</li><li>Online Auctions</li><li>Past Auctions</li></ul></div>
  <div class="fcol contact" style="left:523px"><h4>Contact Us</h4><ul>
    <li><svg width="10" height="10" viewBox="0 0 16 16" aria-hidden="true"><path d="M4 1l3 3-2 2c1 2 3 4 5 5l2-2 3 3-2 2C8 14 2 8 2 3z" fill="#888"/></svg>+1800-555-0193</li>
    <li><svg width="10" height="8" viewBox="0 0 10 8" aria-hidden="true"><rect width="10" height="8" fill="#888"/><path d="M0 0l5 4 5-4" fill="none" stroke="#e4e4e4"/></svg>info@vornehomes.example</li>
    <li style="align-items:flex-start;height:auto;line-height:18px"><svg width="10" height="12" viewBox="0 0 10 12" style="margin-top:3px" aria-hidden="true"><path d="M5 0a4 4 0 0 1 4 4c0 3-4 8-4 8S1 7 1 4a4 4 0 0 1 4-4z" fill="#888"/><circle cx="5" cy="4" r="1.5" fill="#e4e4e4"/></svg><span>Your Address, Your Country<br>Your Zip Code</span></li>
  </ul></div>
  <div class="fcol" style="left:687px"><h4>Social</h4></div>
  <div class="social"><span class="s1"></span><span class="s2"></span><span class="s3"></span><span class="s4"></span></div>
</footer>

<div class="abs bottom">
  <span class="copy">Copyright 2014 © Martin Vorne - All Rights Reserved</span>
  <span class="legal">Site Map &nbsp;&nbsp;•&nbsp;&nbsp; Privacy Policy</span>
</div>
</body>
</html>
```